Tea standup pouch labels

Dear designers,
I need a minimalistic and modern label for my loose tea stand-up pouches (100, 250 and 500gm packs). The label should cover 70-80% of the pouch face (front and rear both).
The label will be 2 part label - Front and Rear side labels.
The labels should have a green background (Pantone Green C) with Golden or White or black colour text. Please either use the Golden logo or black logo to see which looks good with Pantone Green C background.
I am also attaching the content file and a few other files (Assam tea logo) to be used in the label.
The Assam tea logo should be small at the bottom left or right side of the front side. The logo should be dominant on the front page (some of the designs I received have small logo and big "100% single estate tea" and "Assam logo" as big characters on the front page which is not what I am looking for.

The font style should note simple Times new roman or Arial. It should look modern and should be something matching to the logo sentence 'Freshest possible' but should also not be in italics. Please refer to files Font style reference front and back for the style of font. Also use the same box space design on the rear - Content should be in White background; the rectangular box edges should be rounded and the border should be in dual colour - Golden and white or in black and white depending on the logo colour used (golden or black).

For the Rear page - headings could be in Golden colour or black colour depending on the logo colour you choose to use and the text can be in white colour i.e. Option 1 - Headings in golden colour and text in white colour; Option 2 - Heading in Black colour and text in white colour or any other combination that looks good - designer to decide.

Please let me know if you need any further information.

thanks,
Toral

```html
<!DOCTYPE html>
<html lang="en">
<head>
<meta charset="utf-8">
<title>Leafora Tea – Pouch Labels</title>
<link href="https://fonts.googleapis.com/css2?family=Montserrat:wght@400;500;600;700&display=swap" rel="stylesheet">
<style>
  :root{
    --green:#0f5b4c;
    --green-soft:#1d6b5b;
    --green-light:#2a7a69;
    --white:#ffffff;
    --ink:#1c2a26;
    --gold:#d1ae5e;
    --rule:#b9c3bf;
    --page:#e9ecea;
  }
  *{box-sizing:border-box;margin:0;padding:0}
  html,body{width:818px;height:1200px;overflow:hidden;background:var(--page)}
  body{font-family:"Montserrat",Arial,sans-serif;color:var(--white)}
  .sheet{width:818px;height:1200px;display:flex;flex-direction:column;gap:8px}
  .label{position:relative;background:var(--green);overflow:hidden}
  .front{height:540px}
  .rear{flex:1}

  /* front */
  .origin{position:absolute;left:40px;top:36px;font-size:26px;font-weight:700;letter-spacing:.3px}
  .brand{position:absolute;left:80px;top:150px;display:flex;align-items:center;gap:16px}
  .brand-dot{width:20px;height:20px;border-radius:50%;background:var(--white)}
  .brand-name{font-size:58px;font-weight:600;letter-spacing:10px}
  .cup-art{position:absolute;left:40px;top:270px;width:738px;height:200px;border-radius:6px;
    background:linear-gradient(100deg,var(--green-soft) 0%,var(--green-light) 45%,var(--green) 100%)}
  .net-weight{position:absolute;left:40px;bottom:32px;font-size:14px;font-weight:600;letter-spacing:.5px}

  /* rear */
  .rear{padding:28px 36px}
  .rear-title{font-size:25px;font-weight:700;color:var(--gold);padding-bottom:12px;border-bottom:2px solid var(--white)}
  .rear-body{display:flex;gap:30px;margin-top:16px}
  .story{flex:1;font-size:12.5px;line-height:1.5}
  .story p{margin-bottom:8px}
  .story h3{font-size:18px;font-weight:700;color:var(--gold);text-align:center;margin:12px 0 6px}
  .story .taste{font-size:16px;font-weight:600;text-align:center}
  .story ul{list-style:none;margin:4px 0 10px}
  .story li::before{content:"• "}
  .story .fact{font-size:14px;margin-top:10px;line-height:1.45}
  .story .fact b{font-size:16px;font-weight:700;color:var(--gold)}
  .side{width:292px;display:flex;flex-direction:column;gap:16px}
  .info-box{background:var(--white);color:var(--ink);border-radius:12px;border:3px double var(--gold);box-shadow:0 0 0 2px var(--white);padding:12px 14px;font-size:11px}
  .nutrition table{width:100%;border-collapse:collapse}
  .nutrition th{font-size:12px;text-align:left;font-weight:700;border-bottom:2px solid var(--ink);padding-bottom:4px}
  .nutrition td{padding:4px 0;border-bottom:1px solid var(--rule)}
  .nutrition td:last-child{text-align:right;white-space:nowrap}
  .nutrition .note{margin-top:6px;font-size:10px}
  .packer h4{font-size:12.5px;font-weight:700;margin-bottom:5px}
  .packer p{line-height:1.45;margin-bottom:5px}
</style>
</head>
<body>
<main class="sheet">

  <section class="label front">
    <div class="origin">100% Single Estate Tea</div>
    <div class="brand">
      <span class="brand-dot"></span>
      <span class="brand-name">LEAFORA</span>
    </div>
    <div class="cup-art" role="img" aria-label="Line drawing of a steaming tea cup on a saucer with sweeping diagonal steam lines"></div>
    <div class="net-weight">NET WT 250G</div>
  </section>

  <section class="label rear">
    <h2 class="rear-title">Tea loses its flavour and aroma over time</h2>
    <div class="rear-body">
      <div class="story">
        <p>We pack our single estate leaves in small batches so every pouch reaches you fresh. Our growers pick by hand, wither slowly and roll the leaf gently, keeping its natural oils and depth. Open, brew and taste the difference that freshness makes in every cup.</p>
        <h3>What does it taste like?</h3>
        <div class="taste">Strong, malty, astringent taste and aroma</div>
        <h3>How do I drink it?</h3>
        <ul>
          <li>Bring fresh water to a rolling boil</li>
          <li>Add 1 teaspoon of leaves per cup</li>
          <li>Steep for 3 to 5 minutes, then strain</li>
          <li>Add milk or sugar if you like it so</li>
          <li>Enjoy hot, or chill it over ice</li>
        </ul>
        <div class="fact"><b>Ingredients:</b> Black Tea</div>
        <div class="fact"><b>Allergen information:</b><br>Made in a factory that processes nuts.</div>
        <div class="fact"><b>How do I store it:</b><br>Store in an airtight container made of ceramic or tin to keep the light out.</div>
      </div>

      <aside class="side">
        <div class="info-box nutrition">
          <table>
            <tr><th colspan="2">NUTRITIONAL INFORMATION</th></tr>
            <tr><td>Typical values</td><td>per 100ml brewed</td></tr>
            <tr><td>Energy</td><td>1 kcal</td></tr>
            <tr><td>Fat</td><td>0 g</td></tr>
            <tr><td>of which saturates</td><td>0 g</td></tr>
            <tr><td>Carbohydrate</td><td>0.3 g</td></tr>
            <tr><td>of which sugars</td><td>0 g</td></tr>
            <tr><td>Protein</td><td>0.1 g</td></tr>
            <tr><td>Salt</td><td>0 g</td></tr>
          </table>
          <p class="note">Values for tea brewed without milk or sugar.</p>
        </div>
        <div class="info-box packer">
          <h4>Packed in the UK by</h4>
          <p>Leafora Trading Ltd, 14 Orchard Row, Hedgefield, HF2 7QA, United Kingdom</p>
          <p>Visit leaforatea.example</p>
          <p>Best before: see base of pouch</p>
        </div>
      </aside>
    </div>
  </section>

</main>
</body>
</html>
```